Website for Vetra Kolan Holdings

Need a project marketing website for our company which primarily deals in selling real estate(land sales) from Big Estates to Builders /Clients, help them in Building & Construction and do all Project Management.

Coding

Coded - Design and coding required

Number of Pages Required

4 page

Colors
0054AA
0677BA
7BADD7
CADEEF
E8F1F8
FFC000
F8CF3A
FAE287
FDF2CF
FEFAEE

```html
<!DOCTYPE html>
<html lang="en">
<head>
<meta charset="utf-8">
<title>Vetra Kolan Holdings</title>
<link rel="stylesheet" href="https://fonts.googleapis.com/css2?family=Oswald:wght@600;700&family=Poppins:wght@300;400;500;600;700&display=swap">
<style>
:root{
  --blue:#0054AA;
  --blue-mid:#0677BA;
  --blue-soft:#7BADD7;
  --blue-pale:#CADEEF;
  --blue-mist:#E8F1F8;
  --gold:#E89A1C;
  --gold-bright:#FFC000;
  --cream:#FEFAEE;
  --ink:#1b1b1b;
  --muted:#555;
  --white:#fff;
}
*{margin:0;padding:0;box-sizing:border-box}
html,body{width:1200px;height:5316px;overflow:hidden}
body{font-family:'Poppins',sans-serif;color:var(--ink);background:var(--white);position:relative}
.abs{position:absolute}

/* header */
.site-header{position:absolute;left:0;top:0;width:1200px;height:100px;background:var(--white);z-index:3}
.brand{position:absolute;left:68px;top:30px;font-size:32px;font-weight:600;color:var(--blue)}
.main-nav{position:absolute;right:68px;top:36px;display:flex;gap:44px;align-items:center;font-size:17px}
.main-nav a{color:var(--ink);text-decoration:none}
.main-nav .nav-cta{background:var(--blue);color:var(--white);padding:8px 24px;border-radius:24px;margin-top:-8px}

/* hero */
.hero{position:absolute;left:0;top:100px;width:1200px;height:840px;overflow:hidden}
.hero-photo{position:absolute;inset:0;background:linear-gradient(110deg,#3a3d3a 0%,#6d6a60 40%,#a09680 70%,#5a5a4e 100%)}
.hero-shade{position:absolute;inset:0;background:linear-gradient(90deg,rgba(0,0,0,.45),rgba(0,0,0,.05))}
.hero h1{position:absolute;left:68px;top:50px;width:720px;font-family:'Oswald',sans-serif;font-size:72px;line-height:1.55;font-weight:700;color:var(--white);text-transform:uppercase;letter-spacing:.5px}
.hero p{position:absolute;left:68px;top:296px;width:680px;font-size:22px;line-height:1.5;color:var(--white)}
.btn-gold{display:inline-flex;align-items:center;gap:10px;background:var(--gold);color:var(--white);font-weight:500;border-radius:30px;padding:12px 28px;font-size:18px}
.hero .btn-gold{position:absolute;left:68px;top:440px}
.hero-curve{position:absolute;left:0;bottom:0;width:1200px;height:140px}

/* about */
.dot-field{position:absolute;left:20px;top:1040px;width:116px;height:116px;border-radius:50%;background:var(--blue-pale);opacity:.7}
.about-photo-main{position:absolute;left:88px;top:1288px;width:432px;height:392px;border-radius:22px 0 22px 0;background:linear-gradient(135deg,#c9c3b6,#8a8174 60%,#4f4a44)}
.about-photo-small{position:absolute;left:322px;top:1588px;width:204px;height:296px;border-radius:0 0 22px 0;background:linear-gradient(135deg,#d8dde2,#9aa6b2);border:6px solid var(--white)}
.section-title{font-size:50px;font-weight:600;color:var(--blue);line-height:1.2}
.about-title{position:absolute;left:628px;top:1166px}
.eyebrow{position:absolute;left:628px;top:1232px;font-size:15px;letter-spacing:2px;color:var(--gold);font-weight:500}
.eyebrow-rule{position:absolute;left:628px;top:1262px;width:190px;height:3px;background:var(--gold)}
.about-copy{position:absolute;left:628px;top:1314px;width:500px;font-size:14px;line-height:1.75;color:var(--muted)}
.about-copy p{margin-bottom:16px}

/* services */
.services-title{position:absolute;left:68px;top:1990px;width:320px}
.services-intro{position:absolute;left:68px;top:2220px;width:320px;font-size:15px;line-height:1.7;color:var(--muted)}
.service-card{position:absolute;width:348px;height:374px;background:var(--blue);color:var(--white);padding:40px 36px}
.service-card.is-accent{background:linear-gradient(160deg,#f0a531,#d98a12)}
.service-icon{width:80px;height:80px;border-radius:50%;background:var(--gold);display:flex;align-items:center;justify-content:center}
.is-accent .service-icon{background:var(--white)}
.service-card h3{font-size:20px;font-weight:600;margin:22px 0 14px;text-transform:uppercase}
.service-card p{font-size:14px;line-height:1.6;opacity:.92}
.know-more{position:absolute;left:36px;bottom:40px;font-size:14px;font-weight:600;display:flex;gap:10px;align-items:center}

/* what we do */
.wwd-title{position:absolute;left:0;top:2842px;width:1200px;text-align:center}
.process-diagram{position:absolute;left:0;top:2930px;width:1200px;height:640px}
.step-label{position:absolute;font-size:16px;font-weight:600;line-height:1.35;color:var(--ink)}
.team-photo{position:absolute;left:352px;top:3262px;width:500px;height:276px;border-radius:250px 250px 0 0;background:linear-gradient(180deg,#b7c1cc,#6d7884)}

/* testimonials */
.testi-title{position:absolute;left:0;top:3700px;width:1200px;text-align:center}
.testi-lead{position:absolute;left:230px;top:3790px;width:740px;text-align:center;font-size:14px;line-height:1.6;color:var(--muted)}
.testi-card{position:absolute;top:4072px;width:330px;height:240px;background:var(--white);box-shadow:0 6px 24px rgba(0,0,0,.12);border-radius:6px;text-align:center;padding:52px 28px 0}
.avatar{position:absolute;left:50%;top:-30px;margin-left:-30px;width:60px;height:60px;border-radius:50%;background:linear-gradient(135deg,#c4a58a,#7a5c46);border:4px solid var(--white)}
.testi-name{font-size:16px;font-weight:600;color:var(--blue)}
.testi-role{font-size:11px;color:var(--muted);margin-bottom:12px}
.testi-text{font-size:13px;line-height:1.5;color:var(--muted)}
.testi-tag{margin-top:12px;font-weight:600;font-size:14px}
.quote-mark{position:absolute;top:10px;font-size:64px;line-height:1;color:var(--blue-mist)}
.slider-arrow{position:absolute;top:4136px;width:40px;height:40px;border-radius:50%;border:2px solid var(--blue-pale);display:flex;align-items:center;justify-content:center;background:var(--white)}
.dots{position:absolute;left:0;top:4296px;width:1200px;display:flex;justify-content:center;gap:10px}
.dots span{width:12px;height:12px;border-radius:50%;border:2px solid var(--blue)}
.dots span.on{background:var(--blue)}

/* contact */
.contact-title{position:absolute;left:68px;top:4340px}
.contact-lead{position:absolute;left:68px;top:4440px;font-size:15px;color:var(--muted)}
.field{position:absolute;border:1px solid #d7d7d7;font-size:14px;color:var(--muted);padding:12px 16px;background:var(--white)}
.submit-btn{position:absolute;left:68px;top:4780px;background:var(--blue);color:var(--white);font-weight:600;font-size:17px;border-radius:30px;padding:16px 30px;display:flex;gap:10px;align-items:center}
.contact-frame{position:absolute;left:728px;top:4384px;width:420px;height:470px;border:3px solid var(--gold);border-radius:24px}
.contact-photo{position:absolute;left:700px;top:4356px;width:440px;height:470px;border-radius:24px;background:linear-gradient(180deg,#e9efe8,#b8c3b4 55%,#7b7d70)}

/* footer */
.site-footer{position:absolute;left:0;top:4880px;width:1200px;height:404px}
.footer-col{position:absolute;top:140px;color:var(--white)}
.footer-col h4{font-size:20px;font-weight:600;margin-bottom:26px;text-transform:uppercase}
.footer-col ul{list-style:none;font-size:15px;line-height:2.2}
.footer-col li::before{content:"";display:inline-block;width:6px;height:6px;border-radius:50%;background:var(--white);margin-right:14px;vertical-align:middle}
.contact-row{display:flex;gap:14px;align-items:flex-start;font-size:15px;line-height:1.45;margin-bottom:18px}
.contact-row svg{flex:none;margin-top:3px}
.news-input{margin-top:16px;width:210px;height:38px;border:1px solid var(--white);border-radius:20px;position:relative;font-size:13px;padding:9px 16px;opacity:.9}
.news-input span{position:absolute;right:4px;top:4px;width:28px;height:28px;border-radius:50%;background:var(--gold)}
.social{display:flex;gap:14px;margin-top:30px}
.social span{width:38px;height:38px;border-radius:50%;background:var(--gold)}
.copyright{position:absolute;left:0;top:5284px;width:1200px;height:32px;background:var(--gold);color:var(--white);font-size:14px;text-align:center;line-height:32px}
</style>
</head>
<body>

<header class="site-header">
  <div class="brand">Vetra Kolan Holdings</div>
  <nav class="main-nav">
    <a>Home</a><a>About Us</a><a>Our Services</a><a class="nav-cta">Contact us</a>
  </nav>
</header>

<section class="hero">
  <div class="hero-photo" role="img" aria-label="Hand placing a coin on stacks of coins with young plants growing in soil"></div>
  <div class="hero-shade"></div>
  <h1>Build your future with Vetra Kolan!</h1>
  <p>For every building goal, we have the right land parcel to suit your needs. Make your next project work for you – build with Vetra Kolan today!</p>
  <span class="btn-gold">Contact us
    <svg width="16" height="16" viewBox="0 0 16 16"><path d="M3 13L13 3M6 3h7v7" stroke="#fff" stroke-width="2" fill="none"/></svg></span>
  <svg class="hero-curve" viewBox="0 0 1200 140" preserveAspectRatio="none">
    <path d="M0 140 L0 100 Q600 10 1200 60 L1200 140 Z" fill="#fff"/>
    <path d="M0 100 Q600 10 1200 60" stroke="#E89A1C" stroke-width="6" fill="none"/>
  </svg>
</section>

<section class="about">
  <div class="dot-field" role="img" aria-label="Decorative dot pattern"></div>
  <div class="about-photo-main" role="img" aria-label="People reviewing site plans and documents on a desk"></div>
  <div class="about-photo-small" role="img" aria-label="Business meeting with laptop and paperwork"></div>
  <h2 class="section-title about-title">About Us</h2>
  <div class="eyebrow">WHO WE ARE</div>
  <div class="eyebrow-rule"></div>
  <div class="about-copy">
    <p>Vetra Kolan Holdings is a land and development partner working with leading estate owners (Norvane Estates) and offers land sales to builders and clients who want to turn large estates into well planned projects. We also guide our clients through approvals, design and construction so every site reaches its full value.</p>
    <p>The company was founded in the year 2007 and since then has a strong presence in the industry with 500+ clients. Trusted in land sales all across the estates offered by our partners.</p>
    <p>We have a strong backup support of surveyors, engineers and site teams; we customise actionable development plans to suit project goals and budgets for every builder and client.</p>
  </div>
</section>

<section class="services">
  <h2 class="section-title services-title">Our Project Services</h2>
  <div class="services-intro">
    <p>We provide custom based land solutions to help builders and clients grow projects over short or long timelines.</p>
    <p style="margin-top:18px">Get personalised project advice just a click away !</p>
  </div>

  <div class="service-card" style="left:432px;top:2000px">
    <div class="service-icon"><svg width="40" height="40" viewBox="0 0 40 40"><rect x="6" y="22" width="6" height="12" fill="#fff"/><rect x="17" y="14" width="6" height="20" fill="#fff"/><rect x="28" y="6" width="6" height="28" fill="#fff"/></svg></div>
    <h3>Land Sales</h3>
    <p>A ladder to lasting value! Large estates divided into clear, ready parcels for builders and clients. Take Professional Help.</p>
    <div class="know-more">KNOW MORE <svg width="12" height="12" viewBox="0 0 12 12"><path d="M2 10L10 2M4 2h6v6" stroke="#fff" stroke-width="1.6" fill="none"/></svg></div>
  </div>
  <div class="service-card" style="left:792px;top:2000px">
    <div class="service-icon"><svg width="40" height="40" viewBox="0 0 40 40"><path d="M6 34h28M9 30V16M17 30V16M23 30V16M31 30V16M4 14L20 5l16 9z" stroke="#fff" stroke-width="3" fill="none"/></svg></div>
    <h3>Builder Partnerships</h3>
    <p>Vetra Kolan partners with Norvane Estates to match builders with estates that fit their plans, scale and budgets.</p>
    <div class="know-more">KNOW MORE <svg width="12" height="12" viewBox="0 0 12 12"><path d="M2 10L10 2M4 2h6v6" stroke="#fff" stroke-width="1.6" fill="none"/></svg></div>
  </div>
  <div class="service-card" style="left:68px;top:2412px">
    <div class="service-icon"><svg width="40" height="40" viewBox="0 0 40 40"><rect x="8" y="6" width="24" height="28" rx="2" stroke="#fff" stroke-width="3" fill="none"/><path d="M14 14h12M14 20h12M14 26h8" stroke="#fff" stroke-width="3"/></svg></div>
    <h3>Site Approvals</h3>
    <p>Vetra Kolan handles surveys, title checks and permits so every parcel is clear and ready before building starts.</p>
    <div class="know-more">KNOW MORE <svg width="12" height="12" viewBox="0 0 12 12"><path d="M2 10L10 2M4 2h6v6" stroke="#fff" stroke-width="1.6" fill="none"/></svg></div>
  </div>
  <div class="service-card is-accent" style="left:432px;top:2412px">
    <div class="service-icon"><svg width="40" height="40" viewBox="0 0 40 40"><path d="M6 34h28M10 34V18l10-8 10 8v16" stroke="#E89A1C" stroke-width="3" fill="none"/><rect x="17" y="24" width="6" height="10" fill="#E89A1C"/></svg></div>
    <h3>Construction</h3>
    <p>From foundation to finish, our teams build on time and to plan with trusted contractors. Take Professional Help.</p>
    <div class="know-more">KNOW MORE <svg width="12" height="12" viewBox="0 0 12 12"><path d="M2 10L10 2M4 2h6v6" stroke="#fff" stroke-width="1.6" fill="none"/></svg></div>
  </div>
  <div class="service-card" style="left:792px;top:2412px">
    <div class="service-icon"><svg width="40" height="40" viewBox="0 0 40 40"><path d="M20 6L32 11v9c0 7-5 12-12 14C13 32 8 27 8 20v-9z" stroke="#fff" stroke-width="3" fill="none"/><path d="M14 20l4 4 8-8" stroke="#fff" stroke-width="3" fill="none"/></svg></div>
    <h3>Project Management</h3>
    <p>Vetra Kolan manages schedules, budgets and site teams with clear regular reporting from start to handover.</p>
    <div class="know-more">KNOW MORE <svg width="12" height="12" viewBox="0 0 12 12"><path d="M2 10L10 2M4 2h6v6" stroke="#fff" stroke-width="1.6" fill="none"/></svg></div>
  </div>
</section>

<section class="what-we-do">
  <h2 class="section-title wwd-title">What We Do</h2>
  <div class="team-photo" role="img" aria-label="Team of advisors meeting around a laptop"></div>
  <svg class="process-diagram" viewBox="0 2930 1200 640">
    <path d="M240 3540 Q250 3420 368 3268 Q460 3092 604 3068 Q748 3092 832 3268 Q940 3420 948 3540" stroke="#0054AA" stroke-width="3" stroke-dasharray="10 8" fill="none"/>
    <g font-family="Poppins, sans-serif" font-size="26" font-weight="700" fill="#fff" text-anchor="middle">
      <circle cx="252" cy="3468" r="34" fill="#0054AA" stroke="#fff" stroke-width="5"/><text x="252" y="3477">01</text>
      <circle cx="368" cy="3268" r="34" fill="#E89A1C" stroke="#fff" stroke-width="5"/><text x="368" y="3277">02</text>
      <circle cx="604" cy="3068" r="34" fill="#0054AA" stroke="#fff" stroke-width="5"/><text x="604" y="3077">03</text>
      <circle cx="832" cy="3268" r="34" fill="#E89A1C" stroke="#fff" stroke-width="5"/><text x="832" y="3277">04</text>
      <circle cx="944" cy="3468" r="34" fill="#0054AA" stroke="#fff" stroke-width="5"/><text x="944" y="3477">05</text>
    </g>
  </svg>
  <div class="step-label" style="left:80px;top:3436px;width:128px;text-align:right">1st Meeting<br>Intro Meeting &amp;<br>Site Finding</div>
  <div class="step-label" style="left:80px;top:3246px;text-align:right;width:232px">Survey, Evaluation and<br>Land Preparations</div>
  <div class="step-label" style="left:454px;top:2978px;text-align:center;width:300px">2nd Meeting<br>Parcel Presentation</div>
  <div class="step-label" style="left:884px;top:3238px">3rd Meeting<br>Client approved plan<br>implementation</div>
  <div class="step-label" style="left:994px;top:3426px">On going service<br>on Construction<br>Management &amp;<br>Reporting</div>
</section>

<section class="testimonials">
  <h2 class="section-title testi-title">Testimonials</h2>
  <p class="testi-lead">Our clients share what it is like to find, buy and build on land with us, from the first site visit through construction, project management and final handover.</p>
  <div class="slider-arrow" style="left:160px"><svg width="14" height="14" viewBox="0 0 14 14"><path d="M9 2L4 7l5 5" stroke="#0054AA" stroke-width="2" fill="none"/></svg></div>
  <div class="testi-card" style="left:240px">
    <span class="quote-mark" style="left:18px">“</span><span class="quote-mark" style="right:18px">”</span>
    <div class="avatar" role="img" aria-label="Client portrait"></div>
    <div class="testi-name">Daniel Forde</div>
    <div class="testi-role">Managing Director</div>
    <div class="testi-text">I am highly impressed with the personalised service received from Vetra Kolan.</div>
    <div class="testi-tag">Highly recommended!</div>
  </div>
  <div class="testi-card" style="left:630px">
    <span class="quote-mark" style="left:18px">“</span><span class="quote-mark" style="right:18px">”</span>
    <div class="avatar" role="img" aria-label="Client portrait"></div>
    <div class="testi-name">Daniel Forde</div>
    <div class="testi-role">Managing Director</div>
    <div class="testi-text">I am highly impressed with the personalised service received from Vetra Kolan.</div>
    <div class="testi-tag">Highly recommended!</div>
  </div>
  <div class="slider-arrow" style="left:1000px;border-color:var(--blue)"><svg width="14" height="14" viewBox="0 0 14 14"><path d="M5 2l5 5-5 5" stroke="#0054AA" stroke-width="2" fill="none"/></svg></div>
  <div class="dots"><span></span><span></span><span class="on"></span></div>
</section>

<section class="contact">
  <h2 class="section-title contact-title">Contact Us</h2>
  <p class="contact-lead">Please fill out the form below and click submit to contact us. Thank you!</p>
  <div class="field" style="left:68px;top:4528px;width:250px;height:48px">Your Name</div>
  <div class="field" style="left:330px;top:4528px;width:250px;height:48px">Phone Number</div>
  <div class="field" style="left:68px;top:4590px;width:512px;height:48px">Email Address</div>
  <div class="field" style="left:68px;top:4652px;width:512px;height:104px">Message</div>
  <div class="submit-btn">SUBMIT NOW <svg width="14" height="14" viewBox="0 0 14 14"><path d="M2 12L12 2M5 2h7v7" stroke="#fff" stroke-width="2" fill="none"/></svg></div>
  <div class="contact-frame"></div>
  <div class="contact-photo" role="img" aria-label="Glass jar of coins with a young plant sprouting from it"></div>
</section>

<footer class="site-footer">
  <svg class="abs" style="left:0;top:0" width="1200" height="404" viewBox="0 0 1200 404" preserveAspectRatio="none">
    <path d="M0 60 Q600 -20 1200 50 L1200 404 L0 404 Z" fill="#0054AA"/>
    <path d="M0 60 Q600 -20 1200 50" stroke="#E89A1C" stroke-width="8" fill="none"/>
  </svg>
  <div class="footer-col" style="left:216px">
    <h4>Quick Links</h4>
    <ul><li>About Us</li><li>Services</li><li>Testimonials</li><li>Contact Us</li></ul>
  </div>
  <div class="footer-col" style="left:480px">
    <h4>Contact Us</h4>
    <div class="contact-row"><svg width="18" height="18" viewBox="0 0 18 18"><path d="M4 1l3 4-2 2c1 2 3 4 5 5l2-2 4 3-2 3C8 16 2 10 1 4z" fill="#fff"/></svg><span>Call Us<br>(800) 555 0184</span></div>
    <div class="contact-row"><svg width="18" height="18" viewBox="0 0 18 18"><rect x="1" y="3" width="16" height="12" rx="1" stroke="#fff" stroke-width="2" fill="none"/><path d="M1 4l8 6 8-6" stroke="#fff" stroke-width="2" fill="none"/></svg><span>Email Us<br>info@vetrakolan.com</span></div>
    <div class="contact-row"><svg width="18" height="18" viewBox="0 0 18 18"><path d="M9 17s6-6 6-10A6 6 0 0 0 3 7c0 4 6 10 6 10z" fill="#fff"/><circle cx="9" cy="7" r="2" fill="#0054AA"/></svg><span>Address line here<br>Address line two</span></div>
  </div>
  <div class="footer-col" style="left:816px">
    <h4>Our Newsletter</h4>
    <div style="font-size:15px;line-height:1.45">Subscribe our newsletter to<br>get the latest news</div>
    <div class="news-input">Enter Email Address<span></span></div>
    <div class="social"><span></span><span></span><span></span></div>
  </div>
</footer>
<div class="copyright">Copyright © 2024 All Rights Reserved By Vetra Kolan Holdings</div>

</body>
</html>
```